Dumpster rentals winter2019 print ad

Seeking an ad design for use in several local small newspapers. Size of the printed ad will vary slightly so we are looking for a rectangular ad that can be sized by the newspaper to fit their page requirements. see attached sample of an ad from last year a paper created in house. The basic info in the sample ad is what we require. Looking for something a little lighter, easier to read that will appear well in both print and black and white. Humor is OK. We have truck and dumpster photos if you need them.<br/>See our web site for more info: www.haulbinquickva.com and www.haulbinquickbarlow.com and www.pinecrestbinworks.com.
Designer to choose colors to be used in the design.

```html
<!DOCTYPE html>
<html lang="en">
<head>
<meta charset="utf-8">
<title>Roll Off Dumpster Rentals – Pinecrest Bin Works</title>
<link href="https://fonts.googleapis.com/css2?family=Montserrat:ital,wght@0,600;0,700;0,800;0,900;1,600&display=swap" rel="stylesheet">
<style>
  :root {
    --stage: #e9e9e9;
    --paper-top: #ececec;
    --paper-bottom: #ffffff;
    --ink: #1b1b1b;
    --graphite: #4a4a4a;
    --red: #e4000b;
    --red-deep: #b5000a;
    --black: #111111;
    --charcoal: #2b2b2b;
    --yellow: #ffe600;
    --white: #ffffff;
    --truck: #f2c300;
  }
  * { box-sizing: border-box; margin: 0; padding: 0; }
  html, body {
    width: 803px; height: 1200px; overflow: hidden;
    background: var(--stage);
    font-family: "Montserrat", Arial, sans-serif;
  }
  .ad {
    position: absolute; left: 21.5px; top: 144px;
    width: 792px; height: 950px;
    transform: scale(0.96); transform-origin: top left;
    background: linear-gradient(180deg, var(--paper-top) 0%, var(--paper-bottom) 45%);
    box-shadow: 0 12px 30px rgba(0,0,0,.35);
    overflow: hidden;
  }
  .headline { position: absolute; left: 0; right: 0; top: 36px; text-align: center; }
  .headline__kicker {
    font-weight: 800; font-size: 37px; line-height: 1; color: var(--graphite);
    letter-spacing: .5px;
  }
  .headline__main {
    font-weight: 900; font-size: 88px; line-height: .9; color: var(--red);
    letter-spacing: 1px; margin-top: 2px;
  }
  .tags { position: absolute; top: 150px; left: 186px; width: 410px; height: 40px; }
  .tags svg { position: absolute; inset: 0; }
  .tags span {
    position: absolute; top: 0; height: 40px; line-height: 40px;
    font-weight: 800; font-size: 18px; color: var(--white); text-align: center;
  }
  .tags .tag--price { left: 10px; width: 195px; }
  .tags .tag--delivery { left: 205px; width: 195px; }
  .question {
    position: absolute; top: 200px; left: 0; right: 0; text-align: center;
    font-style: italic; font-weight: 600; font-size: 17px; line-height: 24px; color: var(--ink);
  }
  .truck-photo {
    position: absolute; left: 200px; top: 255px; width: 380px; height: 360px;
    background: radial-gradient(ellipse at 55% 55%, var(--truck) 0%, #d8ae00 45%, rgba(60,60,60,.35) 80%, rgba(255,255,255,0) 100%);
    border-radius: 40px;
  }
  .panels { position: absolute; left: 0; top: 0; width: 792px; height: 950px; }
  .brand {
    position: absolute; left: 70px; top: 690px; width: 270px; text-align: center;
    color: var(--white); font-weight: 800; font-size: 34px; line-height: 1.05;
  }
  .brand__mark {
    display: block; width: 34px; height: 34px; margin: 0 auto 12px;
    background: var(--yellow);
  }
  .brand__name small { display: block; font-size: 34px; }
  .pitch {
    position: absolute; left: 420px; top: 680px; width: 372px; text-align: center;
  }
  .pitch__lead { font-weight: 800; font-size: 15.5px; line-height: 23px; color: var(--white); }
  .pitch__cta { font-weight: 900; font-size: 29px; color: var(--yellow); margin-top: 6px; }
  .pitch__pill {
    display: inline-block; margin-top: 12px; padding: 6px 18px;
    background: var(--black); border-radius: 18px;
    color: var(--white); font-weight: 800; font-size: 14px; letter-spacing: .3px;
    box-shadow: 0 4px 6px rgba(0,0,0,.35);
  }
  .phone-bar {
    position: absolute; left: 0; top: 810px; width: 792px; height: 65px;
    background: var(--yellow);
    display: flex; align-items: center; justify-content: center; gap: 14px;
    font-weight: 900; font-size: 23px; color: var(--black);
  }
  .web-bar {
    position: absolute; left: 0; top: 875px; width: 792px; height: 75px;
    background: var(--black);
    display: flex; align-items: center; justify-content: center; gap: 16px;
    font-weight: 600; font-size: 18px; color: var(--white);
  }
  .web-bar .site { display: flex; align-items: center; gap: 8px; }
  .web-bar .site b { color: var(--yellow); font-weight: 700; }
  .web-bar .divider { color: var(--yellow); font-weight: 700; }
</style>
</head>
<body>
<main class="ad">
  <header class="headline">
    <p class="headline__kicker">ROLL OFF DUMPSTER</p>
    <h1 class="headline__main">RENTALS</h1>
  </header>

  <div class="tags">
    <svg viewBox="0 0 410 40" width="410" height="40" aria-hidden="true">
      <defs>
        <linearGradient id="tagRed" x1="0" y1="0" x2="0" y2="1">
          <stop offset="0" stop-color="#ff1a1a"/><stop offset="1" stop-color="#b5000a"/>
        </linearGradient>
        <linearGradient id="tagDark" x1="0" y1="0" x2="0" y2="1">
          <stop offset="0" stop-color="#444"/><stop offset="1" stop-color="#111"/>
        </linearGradient>
      </defs>
      <polygon points="14,0 205,0 193,40 0,40" fill="url(#tagRed)"/>
      <polygon points="212,0 410,0 398,40 200,40" fill="url(#tagDark)"/>
    </svg>
    <span class="tag--price">BEST PRICE!</span>
    <span class="tag--delivery">RAPID DELIVERY!</span>
  </div>

  <p class="question">Need to dispose of junk, trash, construction<br>or demoliton debris quickly?</p>

  <div class="truck-photo" role="img" aria-label="Photo of a yellow dump truck with its bed raised"></div>

  <svg class="panels" viewBox="0 0 792 950" width="792" height="950" aria-hidden="true">
    <defs>
      <linearGradient id="panelBlack" x1="0" y1="0" x2="1" y2="1">
        <stop offset="0" stop-color="#0d0d0d"/><stop offset="1" stop-color="#333"/>
      </linearGradient>
      <linearGradient id="panelRed" x1="0" y1="0" x2="1" y2="1">
        <stop offset="0" stop-color="#ff0a12"/><stop offset="1" stop-color="#a80008"/>
      </linearGradient>
    </defs>
    <polygon points="0,575 420,652 382,810 0,810" fill="url(#panelBlack)"/>
    <polygon points="792,550 420,652 382,810 792,810" fill="url(#panelRed)"/>
  </svg>

  <div class="brand">
    <span class="brand__mark"></span>
    <p class="brand__name">PINECREST<small>BIN WORKS</small></p>
  </div>

  <section class="pitch">
    <p class="pitch__lead">PINECREST BIN WORKS<br>HAS YOUR SOLUTION...</p>
    <p class="pitch__cta">RENT A DUMPSTER!</p>
    <p class="pitch__pill">EASY . TIME-SAVING . AFFORDABLE</p>
  </section>

  <div class="phone-bar">
    <svg width="26" height="26" viewBox="0 0 24 24" aria-hidden="true">
      <path d="M6.6 10.8a15.1 15.1 0 0 0 6.6 6.6l2.2-2.2a1 1 0 0 1 1-.25 11.4 11.4 0 0 0 3.6.57 1 1 0 0 1 1 1V20a1 1 0 0 1-1 1A17 17 0 0 1 3 4a1 1 0 0 1 1-1h3.5a1 1 0 0 1 1 1c0 1.25.2 2.45.57 3.57a1 1 0 0 1-.25 1z" fill="#111"/>
      <path d="M15 3a6 6 0 0 1 6 6M15 6.5A2.5 2.5 0 0 1 17.5 9" stroke="#111" stroke-width="1.8" fill="none" stroke-linecap="round"/>
    </svg>
    <span class="phone-bar__numbers">1-800-55-HAULS (1-800-554-2857) or 555 -01 2-4471</span>
  </div>

  <footer class="web-bar">
    <span class="site">
      <svg width="16" height="16" viewBox="0 0 16 16" aria-hidden="true"><circle cx="8" cy="8" r="7" fill="#ffe600"/><path d="M1 8h14M8 1c-3 3.5-3 10.5 0 14M8 1c3 3.5 3 10.5 0 14" stroke="#111" stroke-width="1" fill="none"/></svg>
      <span>www.<b>haulbinquickbarlow</b>.com</span>
    </span>
    <span class="divider">|</span>
    <span class="site">
      <svg width="16" height="16" viewBox="0 0 16 16" aria-hidden="true"><circle cx="8" cy="8" r="7" fill="#ffe600"/><path d="M1 8h14M8 1c-3 3.5-3 10.5 0 14M8 1c3 3.5 3 10.5 0 14" stroke="#111" stroke-width="1" fill="none"/></svg>
      <span>www.<b>pinecrestbinworks</b>.com</span>
    </span>
  </footer>
</main>
</body>
</html>
```